Local new marketing agency (croatia) need ad design for billboard advertisement dimensions 5x2.4

We are a new company and we are looking for new clients for our led display billboards. We want a slightly provocative with allusion on different things , slightly comical or funny advertisement that will encourage business owners to think that this particular location and our billboard is the right place for them to place their advertisement.It is not mandatory that the advertisement has to be funny.This advertisemet will be on all our locations.Name of company , AMBER SIGNAL . HR

```html
<!DOCTYPE html>
<html lang="hr">
<head>
<meta charset="utf-8">
<title>Amber Signal . HR — Most Wanted Space</title>
<link rel="stylesheet" href="https://fonts.googleapis.com/css2?family=Anton&family=Graduate&family=Jost:wght@500;600&display=swap">
<style>
  :root {
    --page-bg: #ffffff;
    --board-bg: #ffffff;
    --ink-black: #0b0b0b;
    --signal-red: #e00a0a;
    --skin-light: #f1c4a8;
    --skin-mid: #d99a78;
  }
  * { margin: 0; padding: 0; box-sizing: border-box; }
  html, body {
    width: 947px;
    height: 1200px;
    overflow: hidden;
    background: var(--page-bg);
  }
  .canvas {
    position: relative;
    width: 947px;
    height: 1200px;
  }
  .billboard {
    position: absolute;
    left: 63px;
    top: 394px;
    width: 822px;
    height: 411px;
    background: var(--board-bg);
    box-shadow: 0 4px 14px rgba(0, 0, 0, 0.28);
    overflow: hidden;
  }
  .hands {
    position: absolute;
    background: radial-gradient(ellipse at center, var(--skin-mid) 0%, var(--skin-light) 55%, rgba(241, 196, 168, 0) 75%);
    opacity: 0.85;
  }
  .hands--top-left { left: -40px; top: -40px; width: 200px; height: 180px; }
  .hands--top-right { left: 680px; top: -30px; width: 180px; height: 150px; }
  .hands--bottom-left { left: -30px; top: 170px; width: 250px; height: 260px; }
  .hands--bottom-right { left: 620px; top: 160px; width: 230px; height: 270px; }
  .headline {
    position: absolute;
    left: 0;
    right: 0;
    text-align: center;
  }
  .brand-name {
    top: 32px;
    left: 8px;
    font-family: "Jost", sans-serif;
    font-weight: 600;
    font-size: 34px;
    letter-spacing: 0.5px;
    color: var(--ink-black);
  }
  .tagline {
    top: 88px;
    font-family: "Graduate", serif;
    font-size: 70px;
    line-height: 1;
    color: var(--signal-red);
    letter-spacing: 1px;
    transform: scaleX(1.15);
  }
  .offer {
    top: 150px;
    font-family: "Anton", sans-serif;
    font-size: 150px;
    line-height: 1;
    color: var(--ink-black);
    letter-spacing: 2px;
    transform: scaleX(1.05);
  }
  .phone {
    top: 322px;
    font-family: "Jost", sans-serif;
    font-weight: 500;
    font-size: 58px;
    line-height: 1;
    color: var(--signal-red);
  }
</style>
</head>
<body>
  <main class="canvas">
    <section class="billboard">
      <div class="hands hands--top-left" role="img" aria-label="Photo of open hands reaching in from the top-left corner"></div>
      <div class="hands hands--top-right" role="img" aria-label="Photo of open hands reaching in from the top-right corner"></div>
      <div class="hands hands--bottom-left" role="img" aria-label="Photo of open hands reaching in from the bottom-left"></div>
      <div class="hands hands--bottom-right" role="img" aria-label="Photo of open hands reaching in from the bottom-right"></div>

      <p class="headline brand-name">AMBER SIGNAL . HR</p>
      <h1 class="headline tagline">MOST WANTED</h1>
      <h2 class="headline offer">SPACE</h2>
      <p class="headline phone">657.555.0148</p>
    </section>
  </main>
</body>
</html>
```